Product based diagram

Project outline:

We have recently updated our corporate messaging and branding. Our new look is shown on our new website best (www.quorvantel.com).
As you can see the look we have gone for is clean and simple.

Project description:

Image description:

The image needs to reflect complicated product diagram. The current diagram we use runs over several powerpoint slides in order to explain the product. (see process diagram presentation in attachments).
I have attempted to mock up an illustration which could be used as a starting point (see presentation 2).

The successful project will use the POWERPOINT PRESENTATION below as a basis for re-developing our product diagram.

The diagram is based on inputs, out puts and the middle operating system in between.
As seen on our website and the powerpoint the product is based on a number of inputs and outputs, however i would also like to include the 'four pillars' of our product within these:

- smart web forms (these can be shown as one of the inputs)
- CRM/line of business (LoB) integration (input - pulling it and utilising data from a companies existing system - 'making the data immediately actionable')
- Document Automation - (this is technically in the middle, where the action happens)
- data transformation - (the outputs - the transformation of the data through Morevia to any output required)

Image purpose/messaging:

I am looking to have a graphical representation created of our software product to show the products, inputs, outputs, but most importantly as a marketing tool.

This means the diagram needs to be flashy and selling - all within an image

I would like the finished product to include the following:
- An overall diagram image that portrays the product in entirety.
- one or two subsequent images to add further information to the diagram
- reflect our branding and look (as seen on our website) www.quorvantel.com

Please see below for our corporate guidelines and a presentation of the previous diagrams, including the required outputs and inputs.
Updates

Have made some alterations to make the brief a bit clearer!

please submit designs - I'm really excited to see what great ideas are out there!

I welcome all design work here!

Please come check out our new updated brief!

Can't wait to receive your designs

Target Market(s)

leads/prospectives and unknown

Industry/Entity Type

Marketing

Font styles to use
Other font styles liked:
• segoeUI

Requirements
Must have
• clean, and clear images that can help sell the product
logo
refer to branding guidelines and look and feel of new website (www.quorvantel.com) including font (sego UI)

```html
<!DOCTYPE html>
<html lang="en">
<head>
<meta charset="utf-8">
<title>Product Diagram</title>
<link rel="stylesheet" href="https://fonts.googleapis.com/css2?family=Open+Sans:wght@400;600;700&display=swap">
<style>
  :root {
    --bg: #edf0f3;
    --red: #e8473e;
    --green: #34b396;
    --slate: #4a6283;
    --yellow: #f2c318;
    --ink: #1f2328;
    --grey: #8e9296;
    --word: #2b579a;
    --sheet: #217346;
    --slides: #d24726;
    --dark: #2f3b4a;
    --img-green: #17a882;
    --orange: #f7a823;
  }
  * { margin: 0; padding: 0; box-sizing: border-box; }
  html, body { width: 1200px; height: 681px; overflow: hidden; background: var(--bg); }
  body { font-family: "Open Sans", "Segoe UI", sans-serif; color: var(--ink); }
  .diagram { position: relative; width: 1200px; height: 681px; }
  .stage-box {
    position: absolute; top: 79px; width: 192px; height: 349px;
    border: 3px solid; border-radius: 9px; background: #fff;
  }
  .stage-box--inputs { left: 55px; border-color: var(--red); }
  .stage-box--data { left: 345px; top: 71px; border-color: var(--green); }
  .stage-box--content { left: 631px; border-color: var(--slate); }
  .stage-box--output { left: 927px; border-color: var(--yellow); }

  .form-item { position: absolute; left: 0; width: 100%; text-align: center; }
  .form-item svg { display: block; margin: 0 auto; }
  .form-item p { font-size: 16px; line-height: 23px; margin-top: 8px; }
  .form-item--inward { top: 12px; }
  .form-item--outward { top: 184px; }

  .flow-arrow { position: absolute; left: 268px; top: 210px; }

  .source-pill {
    position: absolute; left: 40px; width: 106px; height: 53px; border-radius: 10px;
    background: var(--green); color: #fff; font-weight: 600; font-size: 32px;
    display: flex; align-items: center; justify-content: center; letter-spacing: 0.5px;
  }

  .workflow { position: absolute; left: 552px; top: 187px; width: 66px; text-align: center; }
  .workflow span { display: block; font-size: 14px; margin-top: 4px; color: #333; }

  .content-row { position: absolute; left: 25px; display: flex; align-items: center; gap: 12px; font-size: 19px; font-weight: 600; color: #2d3a4a; }

  .out-icon { position: absolute; }
  .out-code { position: absolute; left: 108px; top: 196px; width: 80px; text-align: center; font-size: 17px; line-height: 25px; color: #2d3a4a; }

  .stage-label { position: absolute; top: 462px; width: 280px; text-align: center; }
  .stage-label h2 { font-size: 34px; font-weight: 600; line-height: 42px; height: 84px; display: flex; flex-direction: column; justify-content: flex-end; }
  .stage-label p { font-size: 22px; margin-top: 17px; }
  .stage-label--inputs { left: 11px; } .stage-label--inputs h2 { color: var(--red); }
  .stage-label--data { left: 298px; top: 446px; } .stage-label--data h2 { color: var(--green); }
  .stage-label--data p { margin-top: 12px; }
  .stage-label--content { left: 585px; } .stage-label--content h2 { color: var(--slate); }
  .stage-label--output { left: 880px; } .stage-label--output h2 { color: var(--yellow); }
</style>
</head>
<body>
<main class="diagram">

  <section class="stage-box stage-box--inputs">
    <div class="form-item form-item--inward">
      <svg width="110" height="96" viewBox="0 0 110 96" aria-hidden="true">
        <rect x="28" y="2" width="72" height="92" rx="4" fill="var(--red)"/>
        <rect x="38" y="12" width="52" height="6" fill="#fff"/>
        <rect x="38" y="26" width="52" height="6" fill="#fff"/>
        <rect x="38" y="40" width="52" height="6" fill="#fff"/>
        <rect x="38" y="54" width="52" height="6" fill="#fff"/>
        <rect x="38" y="68" width="18" height="16" fill="#fff"/>
        <rect x="62" y="68" width="28" height="6" fill="#fff"/>
        <path d="M4 33 L16 46 L4 59 Z M18 33 L30 46 L18 59 Z" fill="#fff" stroke="var(--red)" stroke-width="3" stroke-linejoin="round"/>
      </svg>
      <p>Anonymous<br>inward-facing forms</p>
    </div>
    <div class="form-item form-item--outward">
      <svg width="110" height="96" viewBox="0 0 110 96" aria-hidden="true">
        <rect x="14" y="2" width="72" height="92" rx="4" fill="var(--red)"/>
        <rect x="24" y="12" width="52" height="6" fill="#fff"/>
        <rect x="24" y="26" width="52" height="6" fill="#fff"/>
        <rect x="24" y="40" width="52" height="6" fill="#fff"/>
        <rect x="24" y="54" width="52" height="6" fill="#fff"/>
        <rect x="24" y="68" width="18" height="16" fill="#fff"/>
        <rect x="48" y="68" width="28" height="6" fill="#fff"/>
        <path d="M80 36 L92 49 L80 62 Z M94 36 L106 49 L94 62 Z" fill="#fff" stroke="var(--red)" stroke-width="3" stroke-linejoin="round"/>
      </svg>
      <p>Anonymous<br>outward-facing forms</p>
    </div>
  </section>

  <svg class="flow-arrow" width="56" height="34" viewBox="0 0 56 34" aria-hidden="true">
    <path d="M2 17 H50 M34 3 L50 17 L34 31" fill="none" stroke="var(--grey)" stroke-width="5"/>
  </svg>

  <section class="stage-box stage-box--data">
    <div class="source-pill" style="top:18px">XML</div>
    <div class="source-pill" style="top:99px">SQL</div>
    <div class="source-pill" style="top:180px">ERP</div>
    <div class="source-pill" style="top:261px">NEXA</div>
  </section>

  <div class="workflow">
    <svg width="66" height="80" viewBox="0 0 66 80" aria-hidden="true">
      <path d="M3 3 H46 L63 20 V77 H3 Z" fill="#fff" stroke="var(--red)" stroke-width="4" stroke-linejoin="round"/>
      <path d="M46 3 V20 H63" fill="none" stroke="var(--red)" stroke-width="4"/>
      <rect x="3" y="40" width="8" height="37" fill="var(--red)"/>
      <g transform="translate(24 58)" fill="#444">
        <circle r="8"/>
        <g stroke="#444" stroke-width="4">
          <line x1="0" y1="-12" x2="0" y2="12"/><line x1="-12" y1="0" x2="12" y2="0"/>
          <line x1="-8.5" y1="-8.5" x2="8.5" y2="8.5"/><line x1="-8.5" y1="8.5" x2="8.5" y2="-8.5"/>
        </g>
        <circle r="3.5" fill="#fff"/>
      </g>
    </svg>
    <span>workflow</span>
  </div>

  <section class="stage-box stage-box--content">
    <div class="content-row" style="top:20px">
      <svg width="46" height="56" viewBox="0 0 46 56" aria-hidden="true">
        <path d="M3 3 H30 L43 16 V53 H3 Z" fill="#fff" stroke="#e02020" stroke-width="4" stroke-linejoin="round"/>
        <path d="M30 3 V16 H43" fill="none" stroke="#e02020" stroke-width="3"/>
      </svg>
      PDF
    </div>
    <div class="content-row" style="top:107px">
      <svg width="50" height="50" viewBox="0 0 50 50" aria-hidden="true">
        <rect x="2" y="2" width="46" height="46" fill="#fff" stroke="var(--img-green)" stroke-width="4"/>
        <path d="M8 42 L20 24 L28 34 L34 28 L42 42 Z" fill="var(--img-green)"/>
        <circle cx="36" cy="14" r="4" fill="var(--img-green)"/>
      </svg>
      Images
    </div>
    <div class="content-row" style="top:192px">
      <svg width="50" height="50" viewBox="0 0 50 50" aria-hidden="true">
        <rect x="2" y="2" width="46" height="46" fill="var(--word)"/>
      </svg>
      Scrivo Doc
    </div>
    <div class="content-row" style="top:279px">
      <svg width="50" height="54" viewBox="0 0 50 54" aria-hidden="true">
        <rect x="3" y="3" width="44" height="48" rx="5" fill="#fff" stroke="var(--orange)" stroke-width="4"/>
        <g fill="var(--orange)"><rect x="12" y="14" width="26" height="3"/><rect x="12" y="22" width="26" height="3"/><rect x="12" y="30" width="26" height="3"/><rect x="12" y="38" width="26" height="3"/></g>
      </svg>
      Text
    </div>
  </section>

  <section class="stage-box stage-box--output">
    <svg class="out-icon" style="left:25px;top:23px" width="46" height="60" viewBox="0 0 46 60" aria-hidden="true">
      <path d="M3 3 H30 L43 16 V57 H3 Z" fill="#fff" stroke="#e02020" stroke-width="4" stroke-linejoin="round"/>
      <path d="M30 3 V16 H43" fill="none" stroke="#e02020" stroke-width="3"/>
    </svg>
    <svg class="out-icon" style="left:110px;top:34px" width="66" height="44" viewBox="0 0 66 44" aria-hidden="true">
      <path d="M8 0 H58 Q66 0 66 8 V28 Q66 36 58 36 H30 L24 44 L22 36 H8 Q0 36 0 28 V8 Q0 0 8 0 Z" fill="var(--yellow)"/>
      <text x="33" y="25" text-anchor="middle" font-family="Open Sans, sans-serif" font-size="17" font-weight="600" fill="#fff">SMS</text>
    </svg>
    <svg class="out-icon" style="left:23px;top:105px" width="54" height="54" viewBox="0 0 54 54" aria-hidden="true">
      <rect width="54" height="54" fill="var(--word)"/>
    </svg>
    <svg class="out-icon" style="left:112px;top:105px" width="54" height="54" viewBox="0 0 54 54" aria-hidden="true">
      <rect width="54" height="54" fill="var(--sheet)"/>
    </svg>
    <svg class="out-icon" style="left:22px;top:188px" width="54" height="54" viewBox="0 0 54 54" aria-hidden="true">
      <rect width="54" height="54" fill="var(--slides)"/>
    </svg>
    <div class="out-code">&lt;XML&gt;<br>&lt;html&gt;</div>
    <svg class="out-icon" style="left:25px;top:268px" width="50" height="56" viewBox="0 0 50 56" aria-hidden="true">
      <rect x="3" y="3" width="44" height="50" rx="6" fill="#fff" stroke="var(--dark)" stroke-width="5"/>
      <g fill="var(--dark)"><rect x="13" y="15" width="24" height="4"/><rect x="13" y="24" width="24" height="4"/><rect x="13" y="33" width="24" height="4"/><rect x="13" y="42" width="24" height="3"/></g>
    </svg>
    <svg class="out-icon" style="left:114px;top:278px" width="52" height="38" viewBox="0 0 52 38" aria-hidden="true">
      <rect width="52" height="38" fill="var(--yellow)"/>
      <path d="M0 0 L26 22 L52 0" fill="none" stroke="#fff" stroke-width="3"/>
    </svg>
  </section>

  <div class="stage-label stage-label--inputs"><h2><span>Inputs</span></h2><p>Smart Web Forms</p></div>
  <div class="stage-label stage-label--data"><h2><span>Data</span><span>Integration</span></h2><p>CRM/LOB Integration</p></div>
  <div class="stage-label stage-label--content"><h2><span>Content</span><span>Objects</span></h2><p>Document Automation</p></div>
  <div class="stage-label stage-label--output"><h2><span>Multi-channel</span><span>Output</span></h2><p>Data Transformation</p></div>

</main>
</body>
</html>
```